Design Android App for Creating Estimates and Invoices

This project is to create a graphic design for an Android mobile app called Velmira Contractor App which is an app that will help contractors to quickly create professional estimates and invoices, accept payments, manage clients and projects and run their business smoothly.

Link to some designs I created myself, hoping to get even better design from you
https://pixtray.example/album/qRwoPe

This project is similar to
https://apps.storefrontia.example/details?id=com.bracklyapp.android.brackly
https://apps.storefrontia.example/details?id=com.zeltru.billnote

Check this Google Doc for more information. http://shrtn.example/8KqPmX1

Target Market(s)

Contractors, Home Improvement Professionals, Home Builders,

Industry/Entity Type

Residential Construction

Requirements
Must have
• Non-cluttered screen for Estimates, Enough white space between fields.
Nice to have
• Be different from the two example designs shown

```html
<!DOCTYPE html>
<html lang="en">
<head>
<meta charset="utf-8">
<title>Velmira Contractor App – Screens</title>
<link rel="stylesheet" href="https://fonts.googleapis.com/css2?family=Quicksand:wght@400;500;600;700&display=swap">
<style>
:root{
  --bg:#e9ecef;
  --screen:#fafbfb;
  --brand-blue:#2f6fb5;
  --sky:#27aee6;
  --green:#9dc64b;
  --orange:#ef7f2b;
  --peach:#f6c8a9;
  --ink:#7a7f85;
  --ink-soft:#b3b7bb;
  --line:#c9ccd0;
}
*{box-sizing:border-box;margin:0;padding:0}
html,body{width:1200px;height:1194px;overflow:hidden}
body{background:var(--bg);font-family:"Quicksand",sans-serif;color:var(--ink);position:relative}

.brand{display:flex;align-items:center;gap:12px}
.brand-dot{width:22px;height:22px;border-radius:50%;background:var(--brand-blue)}
.brand-name{font-weight:700;color:var(--brand-blue);letter-spacing:.14em}
.page-brand{position:absolute;left:44px;top:70px}
.page-brand .brand-dot{width:44px;height:44px}
.page-brand .brand-name{font-size:40px}

.screens{position:absolute;left:36px;top:270px;display:flex;gap:24px}
.screen{width:264px;height:620px;background:var(--screen);border-radius:34px;
  box-shadow:0 18px 40px rgba(40,60,80,.12);position:relative;overflow:hidden}

/* splash */
.splash{display:flex;flex-direction:column;align-items:center;justify-content:center;gap:14px}
.splash .brand-name{font-size:30px}
.tagline{font-size:13px;color:var(--ink-soft)}
.spinner{margin-top:24px;width:22px;height:22px;border-radius:50%;border:2px dashed var(--brand-blue)}

/* dashboard */
.dash{padding:34px 20px 0}
.welcome{font-size:15px;color:var(--ink-soft)}
.user-name{font-size:19px;color:var(--sky)}
.avatar{position:absolute;right:20px;top:38px;width:34px;height:34px;border-radius:50%;background:linear-gradient(135deg,#7d8a96,#c4b19c)}
.search{margin-top:16px;height:36px;border-radius:18px;background:#fff;box-shadow:0 6px 16px rgba(40,60,80,.1);display:flex;align-items:center;gap:8px;padding:0 14px;font-size:10px;color:var(--ink-soft)}
.alert{margin-top:14px;height:40px;border-radius:20px;background:var(--peach);display:flex;align-items:center;gap:8px;padding:0 12px;font-size:8.5px;font-weight:700;color:var(--orange)}
.alert-icon{width:20px;height:20px;border-radius:50%;border:1.5px solid var(--orange);display:flex;align-items:center;justify-content:center;font-size:11px}
.resend{display:block;margin:8px 0 0 auto;width:58px;height:22px;border-radius:11px;background:var(--green);color:#fff;font-size:9px;font-weight:700;text-align:center;line-height:22px}
.section-head{display:flex;justify-content:space-between;align-items:baseline;margin-top:10px}
.section-title{font-size:14px;font-weight:700;color:#8a8f94}
.all-link{font-size:9px;color:var(--brand-blue);font-weight:600}
.table{width:100%;border-collapse:collapse;margin-top:6px;font-size:9px}
.table th{font-weight:500;color:var(--ink-soft);text-align:left;padding:3px 0;border-bottom:1px solid #e3e5e7}
.table td{padding:3px 0;color:#8a8f94}
.tabbar{position:absolute;left:0;right:0;bottom:0;height:62px;display:flex;justify-content:space-around;align-items:center;border-top:1px solid #eef0f1}
.tab{display:flex;flex-direction:column;align-items:center;gap:4px;font-size:8px;color:#8a8f94}
.tab.active{color:var(--green)}

/* forms */
.form{padding:70px 26px 0}
.form .brand{justify-content:center;margin-bottom:36px}
.form .brand-name{font-size:22px}
.field{margin-bottom:22px}
.label{font-size:8px;font-weight:700;color:var(--brand-blue);letter-spacing:.05em;text-transform:uppercase}
.input{height:30px;border-bottom:1px solid var(--line);font-size:15px;color:var(--sky);display:flex;align-items:flex-end;justify-content:space-between;padding-bottom:4px}
.input.filled{border-color:var(--brand-blue)}
.input.email{font-size:12.5px}
.forgot{display:block;margin:-12px 0 0 auto;width:50px;height:20px;border-radius:10px;background:var(--green);color:#fff;font-size:8px;text-align:center;line-height:20px;font-weight:700}
.btn{display:block;width:100%;height:46px;border-radius:23px;font-family:inherit;font-size:15px;font-weight:600;text-align:center;line-height:46px}
.btn-primary{background:var(--green);color:#fff;box-shadow:0 10px 20px rgba(157,198,75,.35);margin-top:40px}
.btn-ghost{border:1px solid var(--green);color:var(--green);margin-top:16px}
.back{position:absolute;left:24px;top:28px}
.legal{margin-top:18px;font-size:9px;line-height:1.5;color:#8a8f94;text-align:center}
.legal a{color:var(--green);text-decoration:underline}
</style>
</head>
<body>

<div class="brand page-brand"><span class="brand-dot"></span><span class="brand-name">VELMIRA</span></div>

<main class="screens">

  <section class="screen splash">
    <div class="brand"><span class="brand-dot"></span><span class="brand-name">VELMIRA</span></div>
    <p class="tagline">Customise Your Invoice</p>
    <span class="spinner"></span>
  </section>

  <section class="screen dash">
    <p class="welcome">Welcome</p>
    <p class="user-name">Dariela Stenwick</p>
    <div class="avatar" role="img" aria-label="User profile photo"></div>
    <div class="search">
      <svg width="11" height="11" viewBox="0 0 12 12"><circle cx="5" cy="5" r="3.6" fill="none" stroke="#27aee6" stroke-width="1.6"/><path d="M7.7 7.7 11 11" stroke="#27aee6" stroke-width="1.6"/></svg>
      Search invoices
    </div>
    <div class="alert"><span class="alert-icon">i</span>INVOICE :01245F HAS BEEN REJECTED</div>
    <span class="resend">Resend</span>

    <div class="section-head"><h2 class="section-title">Recent Payments</h2><span class="all-link">all invoices</span></div>
    <table class="table">
      <tr><th>Customer</th><th>Invoice</th><th>Date</th><th>Amount</th></tr>
      <tr><td>John Doe</td><td>#1258F</td><td>Mar 05</td><td>$5220.00</td></tr>
      <tr><td>John Doe</td><td>#1258F</td><td>Feb 07</td><td>$4500.00</td></tr>
      <tr><td>John Doe</td><td>#1258F</td><td>Jan 11</td><td>$6500.00</td></tr>
    </table>

    <div class="section-head"><h2 class="section-title">Upcoming Invoices</h2><span class="all-link">all invoices</span></div>
    <table class="table">
      <tr><th>Customer</th><th>Invoice</th><th>Date</th><th>Amount</th></tr>
      <tr><td>John Doe</td><td>#1258F</td><td>Mar 05</td><td>$5220.00</td></tr>
      <tr><td>John Doe</td><td>#1258F</td><td>Feb 07</td><td>$4500.00</td></tr>
      <tr><td>John Doe</td><td>#1258F</td><td>Jan 11</td><td>$6500.00</td></tr>
    </table>

    <nav class="tabbar">
      <span class="tab active"><svg width="16" height="14" viewBox="0 0 16 14"><path d="M1 13V7l4-3 3 3 4-5 3 3v8z" fill="#9dc64b"/></svg>Activity</span>
      <span class="tab"><svg width="14" height="14" viewBox="0 0 14 14"><rect x="2" y="1" width="10" height="12" rx="1" fill="none" stroke="#8a8f94"/><path d="M4 5h6M4 8h6M4 11h4" stroke="#8a8f94"/></svg>Invoices</span>
      <span class="tab"><svg width="14" height="14" viewBox="0 0 14 14"><path d="M1 6l12-5-5 12-2-5z" fill="none" stroke="#8a8f94"/></svg>Quotations</span>
      <span class="tab"><svg width="14" height="14" viewBox="0 0 14 14"><rect x="1" y="1" width="12" height="12" rx="2" fill="none" stroke="#8a8f94"/><path d="M4 7l2 2 4-4" fill="none" stroke="#8a8f94" stroke-width="1.4"/></svg>Tasks</span>
    </nav>
  </section>

  <section class="screen form">
    <div class="brand"><span class="brand-dot"></span><span class="brand-name">VELMIRA</span></div>
    <div class="field"><p class="label">Email address</p><div class="input filled email">darielastenwick@mail.example</div></div>
    <div class="field"><p class="label">Password</p><div class="input"></div></div>
    <span class="forgot">Forgot?</span>
    <span class="btn btn-primary">Sign in</span>
    <span class="btn btn-ghost">Sign up</span>
  </section>

  <section class="screen form">
    <svg class="back" width="20" height="20" viewBox="0 0 20 20"><path d="M17 17 4 4M4 4v9M4 4h9" fill="none" stroke="#9dc64b" stroke-width="2"/></svg>
    <div class="brand"><span class="brand-dot"></span><span class="brand-name">VELMIRA</span></div>
    <div class="field"><p class="label">Full name</p><div class="input filled">Dariela Stenwick</div></div>
    <div class="field"><p class="label">Email address</p><div class="input"></div></div>
    <div class="field"><p class="label">Select industry</p><div class="input"><span></span><svg width="10" height="8" viewBox="0 0 10 8"><path d="M0 0h10L5 8z" fill="#9dc64b"/></svg></div></div>
    <div class="field"><p class="label">Password</p><div class="input"><span></span><svg width="14" height="10" viewBox="0 0 14 10"><path d="M1 5q6-7 12 0q-6 7-12 0z" fill="none" stroke="#9dc64b"/><circle cx="7" cy="5" r="1.8" fill="#9dc64b"/><path d="M2 9 12 1" stroke="#9dc64b"/></svg></div></div>
    <span class="btn btn-primary" style="margin-top:14px">Sign up</span>
    <p class="legal">By tapping Sign up, you're indicating that you have read and agree to the <a>Privacy Policy</a> and <a>Terms of Service</a></p>
  </section>

</main>
</body>
</html>
```